TR Advisory Business Cards - High End AV / Low Voltage Company

We are low voltage AV company that specializes in high end clients on the residential side and larger businesses on the commercial side. We want something modern, tech looking but also something that is extremely professional looking. We have uploaded our logos and postcards we already have in the field. Along with a picture of one of our wrapped vans. Our website is at www.trvadvisory.example and our primary colors are the orange, green, grey and blue all military color finishes.

We are interesting in the slogans "Pairing You with the Right Technology" or "Clear Signals, Smart Spaces"

Target Market(s)

We focus on 70% Commercial and 30% Residential Customers

Industry/Entity Type

Low Voltage, AV Company

Contact Information for Business Card

Name - Dorian Fairweather, Title - Owner, Office Phone - 555-714-3096, Mobile Phone - 555-802-4173, E-Mail - d@trvadvisory.example, Website: www.trvadvisory.example

Font styles to use
Sans Serif

Requirements
Must have
• Must have Name, Title, Work Phone & Mobile, Website and Logo.
Nice to have
• We want something that will impress our higher end clients with a great logo
Should not have
• Too traditional or plain.

```html
<!DOCTYPE html>
<html lang="en">
<head>
<meta charset="utf-8">
<title>TR Advisory Business Card</title>
<link rel="stylesheet" href="https://fonts.googleapis.com/css2?family=Josefin+Sans:wght@600;700&family=Montserrat:wght@500;700&display=swap">
<style>
  :root {
    --olive: #6b7a4f;
    --olive-dark: #58663f;
    --coral: #ec7f5b;
    --paper: #fbfbfa;
    --ink: #3b3f35;
    --backdrop: #e4e4e1;
  }
  * { box-sizing: border-box; margin: 0; padding: 0; }
  html, body { width: 1200px; height: 900px; overflow: hidden; }
  body {
    background: var(--backdrop);
    display: flex; flex-direction: column; align-items: center; justify-content: center;
    gap: 30px;
    font-family: "Montserrat", sans-serif;
  }
  .card {
    width: 700px; height: 400px; position: relative; overflow: hidden;
    box-shadow: 0 10px 30px rgba(0,0,0,.15);
  }
  /* Front */
  .card-front {
    background: var(--olive);
    display: flex; flex-direction: column; align-items: center; justify-content: center;
  }
  .brand { display: flex; align-items: center; gap: 22px; }
  .brand-dot {
    width: 64px; height: 64px; border-radius: 50%;
    border: 6px solid var(--coral); flex: none;
  }
  .brand-name {
    font-family: "Josefin Sans", sans-serif; font-weight: 700;
    font-size: 58px; color: var(--coral); letter-spacing: 2px;
    text-transform: uppercase; line-height: 1; padding-top: 8px;
    white-space: nowrap;
  }
  .tagline {
    margin-top: 18px; font-family: "Montserrat", sans-serif; font-weight: 700;
    font-size: 13px; letter-spacing: 3px; color: var(--coral); text-transform: uppercase;
  }
  /* Back */
  .card-back { background: var(--paper); }
  .name-band {
    position: absolute; left: 0; top: 78px; width: 420px; height: 64px;
    background: var(--olive-dark);
    clip-path: polygon(0 0, 100% 0, 92% 100%, 0 100%);
  }
  .person-name {
    position: absolute; left: 40px; top: 94px;
    font-family: "Josefin Sans", sans-serif; font-weight: 700;
    font-size: 34px; color: #fff; line-height: 1; white-space: nowrap;
  }
  .person-title {
    position: absolute; left: 40px; top: 156px;
    font-family: "Josefin Sans", sans-serif; font-weight: 700;
    font-size: 28px; color: var(--ink);
  }
  .contact-list {
    position: absolute; left: 430px; top: 160px; list-style: none;
    display: flex; flex-direction: column; gap: 12px;
  }
  .contact-item {
    display: flex; align-items: center; gap: 14px;
    font-size: 16px; font-weight: 500; color: var(--ink); white-space: nowrap;
  }
  .contact-icon {
    width: 22px; height: 22px; border-radius: 50%; background: var(--coral);
    display: flex; align-items: center; justify-content: center; flex: none;
  }
  .contact-icon svg { width: 12px; height: 12px; }
  .back-brand {
    position: absolute; left: 40px; bottom: 34px;
    display: flex; flex-direction: column; align-items: flex-start;
  }
  .back-brand .brand { gap: 14px; }
  .back-brand .brand-dot { width: 40px; height: 40px; border-width: 4px; }
  .back-brand .brand-name { font-size: 34px; }
  .back-brand .tagline { margin-top: 8px; font-size: 9px; letter-spacing: 2px; padding-left: 54px; }
  .accent-strip {
    position: absolute; right: 0; bottom: 0; width: 240px; height: 14px; background: var(--olive);
  }
</style>
</head>
<body>
  <section class="card card-front" aria-label="Card front">
    <div class="brand">
      <span class="brand-dot"></span>
      <span class="brand-name">TR Advisory</span>
    </div>
    <p class="tagline">Clear Signals, Smart Spaces</p>
  </section>

  <section class="card card-back" aria-label="Card back">
    <div class="name-band"></div>
    <h1 class="person-name">Dorian Fairweather</h1>
    <p class="person-title">Owner</p>

    <ul class="contact-list">
      <li class="contact-item">
        <span class="contact-icon"><svg viewBox="0 0 24 24"><path fill="#fff" d="M6.6 10.8a15 15 0 0 0 6.6 6.6l2.2-2.2a1 1 0 0 1 1-.25 11.4 11.4 0 0 0 3.6.57 1 1 0 0 1 1 1V20a1 1 0 0 1-1 1A17 17 0 0 1 3 4a1 1 0 0 1 1-1h3.5a1 1 0 0 1 1 1c0 1.25.2 2.45.57 3.57a1 1 0 0 1-.25 1z"/></svg></span>
        555-714-3096
      </li>
      <li class="contact-item">
        <span class="contact-icon"><svg viewBox="0 0 24 24"><rect x="6" y="2" width="12" height="20" rx="2" fill="none" stroke="#fff" stroke-width="2.5"/><circle cx="12" cy="18" r="1.5" fill="#fff"/></svg></span>
        555-802-4173
      </li>
      <li class="contact-item">
        <span class="contact-icon"><svg viewBox="0 0 24 24"><rect x="2" y="5" width="20" height="14" rx="2" fill="none" stroke="#fff" stroke-width="2.5"/><path d="M3 6l9 7 9-7" fill="none" stroke="#fff" stroke-width="2.5"/></svg></span>
        d@trvadvisory.example
      </li>
      <li class="contact-item">
        <span class="contact-icon"><svg viewBox="0 0 24 24" fill="none" stroke="#fff" stroke-width="2.2"><circle cx="12" cy="12" r="9.5"/><ellipse cx="12" cy="12" rx="4" ry="9.5"/><path d="M2.5 12h19"/></svg></span>
        www.trvadvisory.example
      </li>
    </ul>

    <div class="back-brand">
      <div class="brand">
        <span class="brand-dot"></span>
        <span class="brand-name">TR Advisory</span>
      </div>
      <p class="tagline">Clear Signals, Smart Spaces</p>
    </div>
    <div class="accent-strip"></div>
  </section>
</body>
</html>
```